Postcard Design

We are Bluebridge care. A new way of providing quality healthcare for less. We offer a monthly membership program for $77 per person, $167 per family and cover about 85% of medical conditions. Medical office visits are just $7 each. This innovative program have already saved millions of dollars for it's members in health care costs. We are inviting people to a brief, educational meeting to learn more about how they can save money on their healthcare. We need something catchy and upbeat, positive with 1-2 photos inviting them to come find out more. We will be having appetizers. The date is Wednesday, Feb. 18 drop by between 6-8 pm
Industry/Entity Type
Healthcare

```html
<!DOCTYPE html>
<html lang="en">
<head>
<meta charset="utf-8">
<title>Bluebridge care – Membership Program Postcard</title>
<link rel="stylesheet" href="https://fonts.googleapis.com/css2?family=Gelasio:wght@400;700&family=Arimo&display=swap">
<style>
  :root {
    --backdrop: #c8141c;
    --paper: #ffffff;
    --brand-blue: #0f86b8;
    --brand-orange: #f0901e;
    --ink-grey: #808080;
    --rule-grey: #b9b9b9;
    --photo-people: #e6e2dc;
    --photo-people-deep: #c9c2b8;
    --photo-device: #e9e9e9;
    --photo-device-deep: #c23a3a;
  }
  * { margin: 0; padding: 0; box-sizing: border-box; }
  html, body { width: 782px; height: 1200px; overflow: hidden; }
  body { background: var(--backdrop); font-family: "Gelasio", Georgia, serif; position: relative; }

  .postcard { position: absolute; left: 48px; width: 682px; background: var(--paper); overflow: hidden; }
  .postcard--front { top: 45px; height: 525px; }
  .postcard--back { top: 630px; height: 523px; }

  .brand { position: absolute; display: flex; align-items: center; gap: 8px; color: var(--brand-blue); font-family: "Gelasio", Georgia, serif; font-weight: 700; line-height: 1.05; }
  .brand__dot { width: 22px; height: 22px; border-radius: 50%; background: var(--brand-orange); flex: none; }
  .postcard--front .brand { left: 18px; top: 62px; font-size: 27px; width: 180px; }
  .postcard--back .brand { left: 28px; top: 160px; font-size: 24px; width: 170px; }

  .accent-bar { position: absolute; left: 196px; top: 0; width: 5px; height: 170px; background: var(--brand-orange); }
  .offer { position: absolute; left: 201px; top: 0; width: 481px; height: 170px; background: var(--brand-blue); color: #fff; display: flex; align-items: center; justify-content: center; text-align: center; font-size: 21.5px; line-height: 29px; padding: 0 18px; }
  .offer strong { font-weight: 700; }

  .photo { position: absolute; }
  .photo--team { left: 17px; top: 180px; width: 415px; height: 345px; background: radial-gradient(ellipse at 50% 45%, var(--photo-people) 0%, var(--paper) 75%); }
  .photo--device { left: 22px; top: 240px; width: 265px; height: 150px; background: radial-gradient(ellipse at 60% 50%, var(--photo-device-deep) 0%, var(--photo-device) 45%, var(--paper) 80%); }

  .bubble { position: absolute; border-radius: 50%; display: flex; align-items: center; justify-content: center; text-align: center; font-size: 17.5px; line-height: 25px; }
  .bubble--info { left: 436px; top: 153px; width: 224px; height: 224px; background: var(--brand-orange); color: #222; padding-bottom: 30px; }
  .bubble--date { left: 484px; top: 323px; width: 180px; height: 180px; background: var(--brand-blue); color: #fff; }

  .invite { position: absolute; left: 0; top: 28px; width: 510px; text-align: center; color: var(--brand-orange); font-size: 20px; line-height: 28px; }
  .when { position: absolute; left: 32px; top: 96px; color: var(--brand-blue); font-size: 21px; }

  .stamp { position: absolute; left: 548px; top: 37px; width: 92px; height: 103px; border: 1px dotted var(--ink-grey); color: var(--ink-grey); font-family: "Arimo", Arial, sans-serif; font-size: 15px; line-height: 19px; text-align: center; display: flex; align-items: center; justify-content: center; }

  .address-lines { position: absolute; left: 362px; top: 250px; width: 283px; }
  .address-lines span { display: block; height: 1px; background: var(--rule-grey); margin-bottom: 56px; }
</style>
</head>
<body>
  <section class="postcard postcard--front">
    <div class="brand"><span class="brand__dot"></span><span>Bluebridge care</span></div>
    <div class="accent-bar"></div>
    <div class="offer">
      <p>Monthly Membership Program for <strong>$77</strong> per person, <strong>$167</strong> per family and cover about <strong>85%</strong> of medical conditions. Medical office visits are just <strong>$7</strong> each.</p>
    </div>
    <div class="photo photo--team" role="img" aria-label="Photo of a smiling doctor with a clipboard beside a family of six"></div>
    <div class="bubble bubble--info"><p>Know more<br>about the<br>Monthly Membership<br>Program</p></div>
    <div class="bubble bubble--date"><p>Wednesday,<br>Feb. 18 drop<br>by between<br>6-8 pm</p></div>
  </section>

  <section class="postcard postcard--back">
    <p class="invite">Know more about the<br>Monthly Membership Program</p>
    <p class="when">Wednesday, Feb. 18 drop by between 6-8 pm</p>
    <div class="stamp">Place<br>Stamp<br>Here</div>
    <div class="brand"><span class="brand__dot"></span><span>Bluebridge care</span></div>
    <div class="photo photo--device" role="img" aria-label="Photo of a blood pressure cuff with a red heart"></div>
    <div class="address-lines"><span></span><span></span><span></span></div>
  </section>
</body>
</html>
```